Moss Lantern Sweets Business Card Design

Need a business card design for my eco-luxe dessert company Moss Lantern Sweets. The cards will be printed on 100% post consumer recycled content... so some kind of natural colored paper.

Two sided
Standard Size 2" x 3.5"

Front Content:
Logo
Local. Organic. Sustainable. (underneath logo)

Back Content:
Delia Hurst
Sustainable Pastry Chef
Westport, Connecticut

www.mosslanternsweets.example
mosslanternsweets@mailbox.example
203-571-3064

QR Code (file image)

The cards are going to be printed on recycled paper similar to this color:
HEX: #D5BC84
RGB: 213/188/132

Target Market(s)

Eco-Conscious
Educated
Wealthy
Foodies

Industry/Entity Type

Business

Requirements
Must have
• Two sided Business Card
Standard Size 2" x 3.5"

Front Content:
Logo

Back Content:
Delia Hurst
Sustainable Pastry Chef
203-571-3064
www.mosslanternsweets.example
Westport, Connecticut
*There will also be a QR code. When submitting designs please leave room for the code on the back and I will post the url for the code shortly.
Nice to have
• Earthy Colors (green, brown) with some vibrant oranges/gold

```html
<!DOCTYPE html>
<html lang="en">
<head>
<meta charset="utf-8">
<title>Moss Lantern Sweets — Business Card Front</title>
<link rel="stylesheet" href="https://fonts.googleapis.com/css2?family=Felipa&family=Marcellus&display=swap">
<style>
  :root {
    --paper: #ffffff;
    --card: #d5bc84;
    --ink: #3b2418;
    --script-ink: #4a2814;
    --moss: #7f8b2c;
    --crop: #9a9a9a;
  }
  * { margin: 0; padding: 0; box-sizing: border-box; }
  html, body {
    width: 785px;
    height: 1200px;
    overflow: hidden;
    background: var(--paper);
  }
  .sheet {
    position: relative;
    width: 785px;
    height: 1200px;
  }
  .crop-marks {
    position: absolute;
    inset: 0;
  }
  .crop-marks line {
    stroke: var(--crop);
    stroke-width: 1.4;
  }
  .card {
    position: absolute;
    left: 81px;
    top: 81px;
    width: 623px;
    height: 1039px;
    background: var(--card);
  }
  .brand-dot {
    position: absolute;
    left: 251px;
    top: 190px;
    width: 120px;
    height: 120px;
    border-radius: 50%;
    background: var(--moss);
  }
  .wordmark {
    position: absolute;
    left: 0;
    right: 0;
    top: 400px;
    text-align: center;
    font-family: "Marcellus", serif;
    font-weight: 400;
    color: var(--ink);
    text-transform: uppercase;
  }
  .wordmark-name {
    display: block;
    font-size: 50px;
    line-height: 58px;
    letter-spacing: 0.5px;
  }
  .wordmark-sub {
    display: block;
    font-size: 50px;
    line-height: 58px;
    letter-spacing: 0.5px;
  }
  .tagline {
    position: absolute;
    left: 0;
    right: 0;
    top: 580px;
    text-align: center;
    font-family: "Felipa", cursive;
    font-weight: 400;
    color: var(--script-ink);
    font-size: 84px;
    line-height: 92px;
    list-style: none;
  }
</style>
</head>
<body>
  <div class="sheet">
    <div class="card">
      <div class="brand-dot" aria-hidden="true"></div>
      <h1 class="wordmark">
        <span class="wordmark-name">Moss Lantern</span>
        <span class="wordmark-sub">Sweets</span>
      </h1>
      <ul class="tagline">
        <li>Local</li>
        <li>Organic</li>
        <li>Sustainable</li>
      </ul>
    </div>

    <svg class="crop-marks" width="785" height="1200" viewBox="0 0 785 1200" aria-hidden="true">
      <line x1="81" y1="0" x2="81" y2="58"/>
      <line x1="116" y1="0" x2="116" y2="58"/>
      <line x1="0" y1="81" x2="58" y2="81"/>
      <line x1="0" y1="116" x2="58" y2="116"/>
      <line x1="704" y1="0" x2="704" y2="58"/>
      <line x1="669" y1="0" x2="669" y2="58"/>
      <line x1="727" y1="81" x2="785" y2="81"/>
      <line x1="727" y1="116" x2="785" y2="116"/>
      <line x1="81" y1="1142" x2="81" y2="1200"/>
      <line x1="116" y1="1142" x2="116" y2="1200"/>
      <line x1="0" y1="1120" x2="58" y2="1120"/>
      <line x1="0" y1="1085" x2="58" y2="1085"/>
      <line x1="704" y1="1142" x2="704" y2="1200"/>
      <line x1="669" y1="1142" x2="669" y2="1200"/>
      <line x1="727" y1="1120" x2="785" y2="1120"/>
      <line x1="727" y1="1085" x2="785" y2="1085"/>
    </svg>
  </div>
</body>
</html>
```